Old Shanghai birthday party (1920s - 1930s)

I need an invitation for a joint birthday party; basically we will celebrate a couple: she's turning 40 and he's turning 45). The idea of the venue decoration is very sophisticate, with red lanterns, old style painted paper umbrellas and fans, check it out for your reference
https://www.tackboardly.com/rennavost/jazz-harbour/
Here the details to write down:
Marta and Dennis
are turning 85 !
Come celebrate with us!
Saturday, September 10th, 2016 at 8 pm
Quillberry
7C, 19 Tai Lok Fung Road, Aberdeen, Hong Kong
If you can come, please RSVP to Marta Felcote by August 20th
at (852) 471 26508
Dress code: Old Shanghai

Target Market(s)
Adults around 40 years old (The couple is from Australia)

```html
<!DOCTYPE html>
<html lang="en">
<head>
<meta charset="utf-8">
<title>Marta and Dennis – Old Shanghai Birthday Invitation</title>
<link rel="stylesheet" href="https://fonts.googleapis.com/css2?family=Playball&family=Oswald:wght@600&family=Cormorant+Garamond:wght@500&display=swap">
<style>
  :root {
    --stage: #2a2a2a;
    --border-red: #8f1414;
    --border-red-dark: #6e0d0d;
    --field-red: #c8181a;
    --field-red-bright: #e0221c;
    --field-red-deep: #8a1010;
    --gold: #f3cf63;
    --gold-deep: #d9a93a;
  }
  * { box-sizing: border-box; margin: 0; padding: 0; }
  html, body { width: 1200px; height: 960px; overflow: hidden; }
  body {
    background: var(--stage);
    display: flex; align-items: center; justify-content: center;
  }
  .invitation {
    position: relative;
    width: 1040px; height: 740px;
    background: linear-gradient(135deg, var(--border-red), var(--border-red-dark));
    box-shadow: 0 20px 50px rgba(0,0,0,.55);
  }
  .invitation__field {
    position: absolute; inset: 38px;
    background: radial-gradient(ellipse at 38% 45%, var(--field-red-bright) 0%, var(--field-red) 40%, var(--field-red-deep) 100%);
  }
  .invitation__scenery {
    position: absolute; inset: 0;
    background: radial-gradient(ellipse at 80% 35%, rgba(120,10,10,.35), transparent 55%),
                radial-gradient(ellipse at 30% 20%, rgba(255,90,60,.12), transparent 50%);
  }
  .invitation__frame {
    position: absolute; inset: 38px; pointer-events: none;
  }
  .invitation__content {
    position: absolute; inset: 38px;
    display: flex; flex-direction: column; align-items: center;
    padding-top: 78px;
    color: var(--gold);
    font-family: "Playball", cursive;
    text-align: center;
    text-shadow: 0 1px 2px rgba(80,0,0,.5);
  }
  .greeting { display: flex; flex-direction: column; align-items: center; }
  .greeting__rule { width: 210px; height: 14px; }
  .greeting__line { font-size: 34px; line-height: 1.18; }
  .details { margin-top: 22px; font-size: 32px; line-height: 1.5; }
  .details__venue { margin: 6px 0; }
  .rsvp { font-family: "Oswald", sans-serif; font-weight: 600; font-size: 28px; letter-spacing: .5px; }
  .dress-code {
    margin-top: 16px;
    display: flex; align-items: center; gap: 18px;
    font-family: "Cormorant Garamond", serif; font-weight: 500;
    font-size: 20px; letter-spacing: .5px;
  }
  .dress-code__rule {
    width: 150px; height: 2px;
    background: linear-gradient(90deg, transparent, var(--gold));
  }
  .dress-code__rule--right {
    background: linear-gradient(90deg, var(--gold), transparent);
  }
</style>
</head>
<body>
  <article class="invitation">
    <div class="invitation__field">
      <div class="invitation__scenery" role="img" aria-label="Faint backdrop of red lanterns, painted paper umbrellas and fans in Old Shanghai style"></div>
    </div>

    <svg class="invitation__frame" width="964" height="664" viewBox="0 0 964 664" aria-hidden="true">
      <rect x="18" y="18" width="928" height="628" fill="none" stroke="var(--gold)" stroke-width="3"/>
      <rect x="27" y="27" width="910" height="610" fill="none" stroke="var(--gold-deep)" stroke-width="1.2"/>
    </svg>

    <div class="invitation__content">
      <header class="greeting">
        <svg class="greeting__rule" viewBox="0 0 210 14" aria-hidden="true">
          <line x1="0" y1="12" x2="210" y2="12" stroke="var(--gold)" stroke-width="2"/>
          <circle cx="105" cy="5" r="4" fill="var(--gold)"/>
        </svg>
        <p class="greeting__line">Marta and Dennis</p>
        <p class="greeting__line">are turning 85!</p>
        <p class="greeting__line">Come celebrate with us!</p>
        <svg class="greeting__rule" viewBox="0 0 210 14" aria-hidden="true">
          <line x1="0" y1="2" x2="210" y2="2" stroke="var(--gold)" stroke-width="2"/>
          <circle cx="105" cy="9" r="4" fill="var(--gold)"/>
        </svg>
      </header>

      <section class="details">
        <p class="details__date">Saturday, September 10th, 2016 at 8 pm</p>
        <p class="details__venue">Quillberry</p>
        <p class="details__address">7C, 19 Tai Lok Fung Road, Aberdeen, Hong Kong</p>
        <p class="details__rsvp">If you can come, please <span class="rsvp">RSVP</span> to Marta Felcote by August 20th</p>
        <p class="details__phone">at (852) 471 26508</p>
      </section>

      <p class="dress-code">
        <span class="dress-code__rule" aria-hidden="true"></span>
        <span class="dress-code__text">Dress code: Old Shanghai</span>
        <span class="dress-code__rule dress-code__rule--right" aria-hidden="true"></span>
      </p>
    </div>
  </article>
</body>
</html>
```